Pipe Repair Clamps

A double side A4 showing our pipe repair clamps for stopping leaking pipes within seconds. For water , sewage companies, hotels, malls, airports, hosptals, facilities management companies and district cooling companies. Reverse side will show a size chart. Examples of product uploaded

```html
<!DOCTYPE html>
<html lang="en">
<head>
<meta charset="utf-8">
<title>Pipe Repair Clamps Flyer</title>
<link href="https://fonts.googleapis.com/css2?family=Montserrat:wght@400;600;700;800;900&display=swap" rel="stylesheet">
<style>
  :root {
    --page-bg: #ececec;
    --paper: #ffffff;
    --slate: #4a3e40;
    --slate-dark: #3f3335;
    --coral: #ec7579;
    --cyan: #1fb2d7;
    --gold: #f2b92f;
    --yellow: #f7e625;
    --amber: #f0a42b;
    --ink: #3a3032;
    --icon-bg: #e4e4e6;
    --worker-blue: #2aa6c8;
    --clamp-grey: #c9ccce;
  }
  * { box-sizing: border-box; margin: 0; padding: 0; }
  html, body {
    width: 1200px; height: 1200px; overflow: hidden;
    background: var(--page-bg);
    font-family: "Montserrat", Arial, sans-serif;
  }
  .flyer {
    position: absolute; left: 204px; top: 40px;
    width: 792px; height: 1120px;
    background: var(--paper);
    overflow: hidden;
    box-shadow: 0 10px 30px rgba(0,0,0,0.18);
  }
  .flyer-shapes { position: absolute; inset: 0; }
  .title {
    position: absolute; left: 44px; top: 66px;
    line-height: 0.92; font-weight: 900; text-transform: uppercase;
    white-space: nowrap;
  }
  .title-top { display: block; color: var(--coral); font-size: 54px; letter-spacing: 1px; }
  .title-main { display: block; color: var(--cyan); font-size: 96px; letter-spacing: 1px; }
  .tagline {
    position: absolute; left: 46px; top: 272px;
    color: #fff; text-transform: uppercase; line-height: 1.05;
    white-space: nowrap;
  }
  .tagline-top { display: block; font-weight: 700; font-size: 25px; letter-spacing: 1px; }
  .tagline-main { display: block; font-weight: 900; font-size: 40px; letter-spacing: 1.5px; }
  .worker-art {
    position: absolute; left: 540px; top: 60px; width: 230px; height: 660px;
    border-radius: 115px 115px 20px 20px;
    background: linear-gradient(180deg, #f4c8a0 0%, var(--worker-blue) 28%, #1d8db0 100%);
    opacity: 0.9;
  }
  .features { position: absolute; left: 40px; top: 385px; width: 480px; }
  .feature { display: flex; align-items: center; gap: 20px; height: 100px; }
  .feature-icon {
    flex: none; width: 84px; height: 84px; border-radius: 50%;
    background: radial-gradient(circle, #d7eef5 0%, var(--icon-bg) 60%);
    border: 3px solid #fff;
  }
  .feature-head { color: var(--gold); font-weight: 800; font-size: 19px; margin-bottom: 3px; }
  .feature-text { color: #fff; font-weight: 700; font-size: 13.5px; line-height: 1.3; }
  .clamp-photo {
    position: absolute; left: 60px; top: 808px; width: 200px; height: 190px;
    border-radius: 50%;
    background: radial-gradient(circle, rgba(0,0,0,0) 42%, var(--clamp-grey) 44%, #a7abae 60%, rgba(0,0,0,0) 62%);
  }
  .body-copy {
    position: absolute; left: 320px; top: 822px;
    color: var(--ink); font-size: 14px; line-height: 1.25; font-weight: 400;
    white-space: nowrap;
  }
  .contacts {
    position: absolute; left: 40px; right: 40px; top: 1040px;
    display: flex; justify-content: space-between; align-items: center;
    color: #fff; font-size: 14.5px; font-weight: 600;
  }
  .contact { display: flex; align-items: center; gap: 7px; }
  .contact svg { width: 13px; height: 13px; fill: var(--gold); }
</style>
</head>
<body>
  <article class="flyer">
    <svg class="flyer-shapes" viewBox="0 0 792 1120" preserveAspectRatio="none" aria-hidden="true">
      <defs>
        <linearGradient id="bandGradient" x1="0" x2="1" y1="0" y2="0">
          <stop offset="0" stop-color="var(--amber)"/>
          <stop offset="0.35" stop-color="var(--yellow)"/>
          <stop offset="1" stop-color="var(--yellow)"/>
        </linearGradient>
      </defs>
      <path d="M0 248 C 250 220, 520 180, 792 150 L792 1120 L0 1120 Z" fill="var(--slate)"/>
      <path d="M0 840 L792 765 L792 960 L0 1000 Z" fill="url(#bandGradient)"/>
      <path d="M0 1000 L792 960 L792 1120 L0 1120 Z" fill="var(--slate-dark)"/>
      <ellipse cx="655" cy="718" rx="130" ry="24" fill="#bdbcbe"/>
    </svg>

    <h1 class="title">
      <span class="title-top">Pipe Repair</span>
      <span class="title-main">Clamps</span>
    </h1>

    <p class="tagline">
      <span class="tagline-top">Stopping leaking pipes</span>
      <span class="tagline-main">Within seconds</span>
    </p>

    <div class="worker-art" role="img" aria-label="Illustration of a smiling plumber in blue overalls and cap holding a pipe wrench and a flag pole"></div>

    <section class="features">
      <div class="feature">
        <div class="feature-icon" role="img" aria-label="Icon of a plumber kneeling at work"></div>
        <div>
          <h2 class="feature-head">Hedline</h2>
          <p class="feature-text">Text for Examples of product Text for<br>Examples of product Text for Examples of<br>product Text for Examples of product</p>
        </div>
      </div>
      <div class="feature">
        <div class="feature-icon" role="img" aria-label="Icon of a plumber fixing a pipe with a wrench"></div>
        <div>
          <h2 class="feature-head">Hedline</h2>
          <p class="feature-text">Text for Examples of product Text for<br>Examples of product Text for Examples of<br>product Text for Examples of product</p>
        </div>
      </div>
      <div class="feature">
        <div class="feature-icon" role="img" aria-label="Icon of a pipe valve"></div>
        <div>
          <h2 class="feature-head">Hedline</h2>
          <p class="feature-text">Text for Examples of product Text for<br>Examples of product Text for Examples of<br>product Text for Examples of product</p>
        </div>
      </div>
      <div class="feature">
        <div class="feature-icon" role="img" aria-label="Icon of a leaking sink pipe"></div>
        <div>
          <h2 class="feature-head">Hedline</h2>
          <p class="feature-text">Text for Examples of product Text for<br>Examples of product Text for Examples of<br>product Text for Examples of product</p>
        </div>
      </div>
    </section>

    <div class="clamp-photo" role="img" aria-label="Photo of a galvanised steel pipe repair clamp"></div>

    <p class="body-copy">
      Text for Examples of product Text for Examples of product<br>
      Text for Examples of product Text for Examples of product<br>
      Text for Examples of product Text for Examples of product<br>
      Text for Examples of product Text for Examples of product<br>
      Text for Examples of product Text for Examples of product<br>
      Text for Examples of product Text for Examples of product<br>
      Text for Examples of product Text for Examples of product<br>
      Text for Examples of product Text for Examples of product
    </p>

    <footer class="contacts">
      <span class="contact">
        <svg viewBox="0 0 16 16"><path d="M3 1l3 3-1.5 2a9 9 0 0 0 5.5 5.5L12 10l3 3-2 2C7 15 1 9 1 3z"/></svg>
        + 00 000 000 000
      </span>
      <span class="contact">
        <svg viewBox="0 0 16 16"><path d="M1 3h14v10H1z M1 3l7 6 7-6" stroke="#4a3e40" stroke-width="1"/></svg>
        @mail
      </span>
      <span class="contact">
        <svg viewBox="0 0 16 16"><path d="M8 0a5.5 5.5 0 0 0-5.5 5.5C2.5 10 8 16 8 16s5.5-6 5.5-10.5A5.5 5.5 0 0 0 8 0zm0 8a2.5 2.5 0 1 1 0-5 2.5 2.5 0 0 1 0 5z"/></svg>
        your address
      </span>
      <span class="contact">
        <svg viewBox="0 0 16 16"><circle cx="8" cy="8" r="7" fill="none" stroke="var(--gold)" stroke-width="1.6"/><path d="M1 8h14M8 1c-3 3-3 11 0 14M8 1c3 3 3 11 0 14" fill="none" stroke="var(--gold)" stroke-width="1.4"/></svg>
        www.com
      </span>
    </footer>
  </article>
</body>
</html>
```